New Business Card Design Project

Hi! I would like for you to design a business card for our aesthetic injections business. We offer Zelvia, filler, skin care. I would like it to be elegant, feminine, modern and sleek/clean. I like black/gold foil/ivory/parchment colors. It can be either one or two sided. I would like matte black with gold foil logo on one side and ivory with gold foil information on the other side

Target Market(s)

target market is the discerning woman who wants to look her best

Industry/Entity Type

beauty

Contact Information for Business Card

logo, name, phone, email, website, instagram, facebook, location

Requirements
Must have
• logo and info
Nice to have
• the icons for cell, instagram, email, fb etc
Should not have
• images of people

```html
<!DOCTYPE html>
<html lang="en">
<head>
<meta charset="utf-8">
<title>Velora Skin Studio – Business Card</title>
<link href="https://fonts.googleapis.com/css2?family=Roboto:wght@400;500;700&display=swap" rel="stylesheet">
<style>
  :root {
    --backdrop: #c4bab5;
    --ivory: #eadbc2;
    --gold-dark: #b9782a;
    --gold: #c98f3c;
    --gold-light: #e0ad5c;
    --text-gold: #b87526;
    --white: #fffaf0;
  }
  * { box-sizing: border-box; margin: 0; padding: 0; }
  html, body {
    width: 1200px; height: 927px; overflow: hidden;
    background: var(--backdrop);
    font-family: "Roboto", Arial, sans-serif;
  }
  .canvas {
    width: 1200px; height: 927px;
    display: flex; align-items: center; justify-content: center; gap: 60px;
  }
  .card {
    position: relative;
    width: 520px; height: 297px;
    background: var(--ivory);
    box-shadow: 0 10px 24px rgba(80, 60, 50, 0.18);
  }
  /* Info side */
  .info-block {
    position: absolute; top: 78px; left: 0; right: 0;
    display: flex; justify-content: center; align-items: center;
    color: var(--text-gold);
  }
  .identity {
    text-align: right; padding-right: 14px;
    border-right: 1px solid var(--gold-light);
  }
  .identity .name { font-weight: 700; font-size: 19px; letter-spacing: 0.3px; }
  .identity .title { font-size: 13px; margin-top: 2px; }
  .identity .address { font-size: 13px; line-height: 1.35; margin-top: 6px; }
  .contacts { list-style: none; padding-left: 14px; font-size: 13px; line-height: 1.45; }
  .contacts li { display: flex; align-items: center; gap: 6px; }
  .contacts svg { width: 10px; height: 10px; flex: none; }
  .foil-band {
    position: absolute; left: 0; right: 0; top: 206px; height: 30px;
    background: linear-gradient(90deg, var(--gold-dark), var(--gold-light) 35%, var(--gold) 60%, var(--gold-light) 85%, var(--gold-dark));
    display: flex; align-items: center; justify-content: center;
  }
  .foil-band .website {
    color: var(--white); font-weight: 700; font-size: 12px; letter-spacing: 3.5px; text-transform: uppercase;
  }
  /* Brand side */
  .brand {
    position: absolute; inset: 0;
    display: flex; align-items: center; justify-content: center; gap: 12px;
    color: var(--text-gold);
  }
  .brand-dot {
    width: 18px; height: 18px; border: 1.5px solid var(--text-gold); border-radius: 50%;
  }
  .brand-name {
    font-weight: 500; font-size: 22px; letter-spacing: 5px; text-transform: uppercase;
  }
</style>
</head>
<body>
<main class="canvas">
  <section class="card card-info">
    <div class="info-block">
      <div class="identity">
        <div class="name">DANIEL HART</div>
        <div class="title">President</div>
        <div class="address">412 Linden Court<br>Fairview, Oregon 97024</div>
      </div>
      <ul class="contacts">
        <li>
          <svg viewBox="0 0 10 10" aria-hidden="true"><path d="M2 1 L4 1 L4.6 3 L3.4 4 Q4.4 5.8 6 6.6 L7 5.4 L9 6 L9 8 Q8.5 9 7.5 9 Q1 8 1 2.5 Q1 1.5 2 1 Z" fill="currentColor"/></svg>
          555-014-2287
        </li>
        <li>
          <svg viewBox="0 0 10 10" aria-hidden="true"><rect x="0.5" y="2" width="9" height="6.5" fill="currentColor"/><path d="M0.5 2 L5 5.5 L9.5 2" stroke="#eadbc2" stroke-width="0.9" fill="none"/></svg>
          hello@velorastudio.com
        </li>
        <li>
          <svg viewBox="0 0 10 10" aria-hidden="true"><circle cx="5" cy="5" r="4.5" fill="currentColor"/></svg>
          /velorastudio
        </li>
        <li>
          <svg viewBox="0 0 10 10" aria-hidden="true"><circle cx="5" cy="5" r="4.5" fill="currentColor"/></svg>
          @velorastudio
        </li>
      </ul>
    </div>
    <div class="foil-band"><span class="website">www.velorastudio.com</span></div>
  </section>

  <section class="card card-brand">
    <div class="brand">
      <span class="brand-dot"></span>
      <span class="brand-name">Velora Skin Studio</span>
    </div>
  </section>
</main>
</body>
</html>
```